New IT recruitment and consulting company need web logo.

We need a web logo design for a new company based in Scandinavia called "Taku".
We work with recruitment and management consulting within HR and strategy mainly for the IT industry in Scandinavia. Long experience from recruitment and the IT industry.
We would like to see designs that use the color orange. The design should communicate trust, enthusiasm, success and energy.

Target Market(s)

CEO and line managers in the potential customer companies.

Industry/Entity Type

Management Consulting

Number of Pages Required

1 page

Font styles to use
Sans Serif

Requirements
Must have
• Modern web design.
Nice to have
• We would like to see designs that use the color orange.

```html
<!DOCTYPE html>
<html lang="en">
<head>
<meta charset="utf-8">
<title>Taku — Recruitment &amp; Management Consulting</title>
<link rel="stylesheet" href="https://fonts.googleapis.com/css2?family=Montserrat:wght@300;400;600;700&family=Open+Sans:ital,wght@0,400;0,600;0,700;1,400&display=swap">
<style>
:root{
  --orange:#e2580f;
  --orange-dark:#c94a08;
  --ink:#333;
  --muted:#666;
  --line:#d9d9d9;
  --grey-bg:#f3f3f3;
  --footer:#333;
  --footer-bottom:#262626;
  --white:#fff;
}
*{box-sizing:border-box;margin:0;padding:0}
html,body{width:1200px;height:2166px;overflow:hidden}
body{position:relative;background:var(--white);font-family:"Open Sans",Arial,sans-serif;color:var(--ink)}
.abs{position:absolute}
.heading{font-family:"Montserrat",Arial,sans-serif;font-weight:700;color:var(--orange);font-size:28px;letter-spacing:.3px}
.brand{font-family:"Montserrat",Arial,sans-serif;font-weight:600;color:var(--orange)}

/* header */
.top-rule{left:0;top:0;width:1200px;height:3px;background:var(--orange)}
.header-logo{left:85px;top:46px;font-size:50px;line-height:1}
.social{display:flex;gap:6px}
.social span{width:29px;height:29px;border-radius:50%;display:block}
.s1{background:#3b5b9a}.s2{background:#1f7bb6}.s3{background:#f0a030}
.phone-badge{width:29px;height:29px;border-radius:50%;background:#e8383d;display:flex;align-items:center;justify-content:center}
.phone-top{left:1013px;top:38px;font-size:14px;font-weight:600;color:#222}
.nav{left:618px;top:78px;display:flex;align-items:center;font-size:14px;color:#444}
.nav a{color:inherit;text-decoration:none;padding:0 24px;border-left:1px solid #bbb;line-height:18px}
.nav a.active{background:var(--orange);color:#fff;border:none;padding:0 22px;line-height:34px;border-radius:2px;margin-right:18px}
.nav a.active+a{border-left:none}

/* hero */
.hero{left:0;top:128px;width:1200px;height:514px;background:linear-gradient(100deg,#6d5a52 0%,#a77a5c 30%,#d99a62 55%,#b86f45 75%,#5a3a2e 100%)}
.hero-title{left:87px;top:332px;color:#fff;font-family:"Montserrat",Arial,sans-serif;font-size:28px;line-height:36px}
.hero-title b{font-weight:700;display:block}
.hero-title span{font-weight:300;display:block}
.hero-text{left:90px;top:401px;width:430px;color:#fff;font-size:13px;line-height:21px}
.hero-btn{left:90px;top:455px;width:133px;height:40px;background:var(--orange);color:#fff;font-size:14px;line-height:40px;text-align:center;border-radius:2px}
.hero-arrow{top:356px}

/* welcome */
.welcome-title{left:0;top:687px;width:1200px;text-align:center}
.rule{height:2px;background:#555}
.welcome-text{left:130px;top:755px;width:940px;text-align:center;font-size:12px;line-height:24px;color:#555}
.service{width:230px;text-align:center}
.service .ring{width:118px;height:118px;border:1.5px solid #777;border-radius:50%;margin:0 auto;display:flex;align-items:center;justify-content:center}
.service .ring.hot{border-color:var(--orange)}
.service h3{font-weight:400;font-size:16px;margin-top:20px;color:#333}
.service p{font-size:12px;line-height:20.5px;color:#555;margin:8px auto 0;width:200px}

/* why / testimonials */
.band-grey{left:0;top:1121px;width:1200px;height:391px;background:var(--grey-bg)}
.why-text{left:87px;top:1241px;width:380px;font-size:12px;line-height:24px;color:#555}
.checks{font-size:12px;color:#444;list-style:none}
.checks li{display:flex;align-items:center;gap:12px;height:25px}
.tick{width:14px;height:14px;border-radius:50%;background:var(--orange);display:flex;align-items:center;justify-content:center}
.read-more{left:85px;top:1406px;font-size:13px;color:var(--orange);text-decoration:underline}
.quote{left:573px;top:1254px;width:480px;font-size:12px;line-height:24px;color:#777;font-style:italic}
.qmark{font-family:Georgia,serif;font-size:40px;color:#ccc;line-height:1}
.avatar{left:558px;top:1342px;width:90px;height:90px;border-radius:50%;background:linear-gradient(180deg,#dcdcdc,#9aa3ad);border:3px solid #fff;box-shadow:0 0 0 1px #ddd}
.person-name{left:667px;top:1374px;font-size:11px;font-weight:700;color:var(--orange)}
.person-role{left:667px;top:1395px;font-size:11px;color:#444}
.dots{left:972px;top:1390px;display:flex;gap:3px}
.dots span{width:11px;height:11px;border-radius:50%;background:#ccc}

/* customers */
.customer-title{left:0;top:1567px;width:1200px;text-align:center}
.client{top:1638px;width:176px;height:99px;border:5px solid #eee;display:flex;align-items:center;justify-content:center;font-family:"Open Sans",Arial,sans-serif;font-weight:600;font-size:24px;color:#555}

/* contact band */
.contact-band{left:0;top:1790px;width:1200px;height:65px;background:var(--orange)}
.cb-item{display:flex;align-items:center;gap:18px;color:#fff;font-size:13px}
.cb-icon{width:36px;height:36px;border:2px solid #fff;border-radius:50%;display:flex;align-items:center;justify-content:center;flex:none}

/* footer */
.footer{left:0;top:1855px;width:1200px;height:265px;background:var(--footer)}
.footer-logo{left:85px;top:1894px;font-size:54px;color:#fff;line-height:1}
.footer-text{left:85px;top:1996px;width:250px;font-size:12px;line-height:22px;color:#eee}
.col-title{font-family:"Montserrat",Arial,sans-serif;font-weight:400;font-size:19px;color:#fff}
.col-rule{width:126px;height:1px;background:#777;margin-top:6px}
.links{list-style:none;margin-top:14px;font-size:12px;color:#ddd}
.links li{height:31px;display:flex;align-items:center;gap:10px}
.links li::before{content:"›";color:#ccc;font-size:14px}
.divider{width:1px;background:#444;top:1900px;height:190px}
.map{left:877px;top:1930px;width:240px;height:153px;background:linear-gradient(135deg,#f3efe2,#e8e2cd 60%,#f0d86c);border:4px solid #fff}
.bottom-bar{left:0;top:2120px;width:1200px;height:46px;background:var(--footer-bottom)}
.copyright{left:85px;top:2135px;font-size:12px;color:#ccc}
.bottom-social{left:1003px;top:2128px;display:flex;gap:6px}
</style>
</head>
<body>

<!-- Header -->
<div class="abs top-rule"></div>
<div class="abs brand header-logo">Taku</div>
<div class="abs social" style="left:866px;top:32px"><span class="s1"></span><span class="s2"></span><span class="s3"></span></div>
<div class="abs phone-badge" style="left:978px;top:33px">
  <svg width="12" height="16" viewBox="0 0 12 16"><rect x="1.5" y="1" width="9" height="14" rx="1.5" fill="none" stroke="#fff" stroke-width="1.6"/><circle cx="6" cy="12.3" r="0.9" fill="#fff"/></svg>
</div>
<div class="abs phone-top">(555)-210-4800</div>
<nav class="abs nav">
  <a class="active" href="#">Home</a><a href="#">About us</a><a href="#">Services</a><a href="#">Solutions</a><a href="#" style="padding-right:0">Options</a>
</nav>

<!-- Hero -->
<div class="abs hero" role="img" aria-label="Sunset photo of two climbers silhouetted on a rock, one helping the other up"></div>
<svg class="abs hero-arrow" style="left:30px" width="22" height="60" viewBox="0 0 22 60"><polyline points="18,4 4,30 18,56" fill="none" stroke="#fff" stroke-width="1.5"/></svg>
<svg class="abs hero-arrow" style="left:1148px" width="22" height="60" viewBox="0 0 22 60"><polyline points="4,4 18,30 4,56" fill="none" stroke="#fff" stroke-width="1.5"/></svg>
<div class="abs hero-title"><b>RECRUITMENT &amp; MANAGEMENT</b><span>CONSULTING</span></div>
<p class="abs hero-text">Nemo enim ipsam voluptatem quia voluptas sit aspernatur aut odit aut fugit, sed quia consequuntur magni dolores</p>
<div class="abs hero-btn">Read more info</div>

<!-- Welcome -->
<h2 class="abs heading welcome-title">WELCOME TO TAKU</h2>
<div class="abs rule" style="left:457px;top:733px;width:286px"></div>
<p class="abs welcome-text">Lorem Ipsum is simply dummy text of the printing and typesetting industry. Lorem Ipsum has been the industry's standard dummy text ever since the 1500s, when an unknown printer took a galley of type and scrambled it to make a type specimen book.</p>

<div class="abs service" style="left:83px;top:838px">
  <div class="ring"><svg width="54" height="54" viewBox="0 0 54 54" fill="none" stroke="#555" stroke-width="1.6"><path d="M19 30a10 10 0 1 1 16 0c-2 3-3 5-3 8H22c0-3-1-5-3-8z"/><line x1="22" y1="42" x2="32" y2="42"/><line x1="23" y1="46" x2="31" y2="46"/><line x1="27" y1="4" x2="27" y2="9"/><line x1="10" y1="12" x2="14" y2="16"/><line x1="44" y1="12" x2="40" y2="16"/><line x1="5" y1="27" x2="10" y2="27"/><line x1="44" y1="27" x2="49" y2="27"/></svg></div>
  <h3>Recruitment</h3>
  <p>Pain can procure him some great pleasure. To take a trivial example, which of us ever takes</p>
</div>
<div class="abs service" style="left:345px;top:838px">
  <div class="ring"><svg width="56" height="56" viewBox="0 0 56 56" fill="none" stroke="#555" stroke-width="1.6"><rect x="6" y="22" width="8" height="24"/><rect x="16" y="12" width="8" height="34"/><rect x="26" y="16" width="8" height="30"/><circle cx="36" cy="34" r="9"/><line x1="42.5" y1="40.5" x2="51" y2="49"/></svg></div>
  <h3>Management consulting</h3>
  <p>Pain can procure him some great pleasure. To take a trivial example, which of us ever takes</p>
</div>
<div class="abs service" style="left:606px;top:838px">
  <div class="ring hot"><svg width="56" height="56" viewBox="0 0 56 56" fill="none" stroke="#e2580f" stroke-width="1.8"><rect x="8" y="10" width="36" height="36" rx="3"/><rect x="13" y="15" width="26" height="26" rx="2"/><polyline points="18,28 25,35 48,10"/></svg></div>
  <h3>Hr and Strategy</h3>
  <p>Pain can procure him some great pleasure. To take a trivial example, which of us ever takes</p>
</div>
<div class="abs service" style="left:868px;top:838px">
  <div class="ring"><svg width="56" height="56" viewBox="0 0 56 56" fill="none" stroke="#555" stroke-width="1.6"><path d="M24 6h8l1 6 5 2 5-4 6 6-4 5 2 5 6 1v8l-6 1-2 5 4 5-6 6-5-4-5 2-1 6h-8l-1-6-5-2-5 4-6-6 4-5-2-5-6-1v-8l6-1 2-5-4-5 6-6 5 4 5-2z"/><circle cx="28" cy="28" r="8"/></svg></div>
  <h3>Selection System</h3>
  <p>Pain can procure him some great pleasure. To take a trivial example, which of us ever takes</p>
</div>

<!-- Why choose us / Testimonials -->
<div class="abs band-grey"></div>
<h2 class="abs heading" style="left:87px;top:1185px">WHY CHOOSE US</h2>
<div class="abs rule" style="left:87px;top:1226px;width:255px;height:1px"></div>
<p class="abs why-text">Lorem Ipsum is simply dummy text of the printing and typesetting industry. Lorem Ipsum has been the industry's standard dummy text ever since the 1500s, when an unknown printer</p>
<ul class="abs checks" style="left:87px;top:1321px">
  <li><span class="tick"><svg width="8" height="8" viewBox="0 0 8 8"><polyline points="1,4 3.2,6 7,1.5" fill="none" stroke="#fff" stroke-width="1.5"/></svg></span>Industry Expertise</li>
  <li><span class="tick"><svg width="8" height="8" viewBox="0 0 8 8"><polyline points="1,4 3.2,6 7,1.5" fill="none" stroke="#fff" stroke-width="1.5"/></svg></span>Guaranteed hire</li>
  <li><span class="tick"><svg width="8" height="8" viewBox="0 0 8 8"><polyline points="1,4 3.2,6 7,1.5" fill="none" stroke="#fff" stroke-width="1.5"/></svg></span>Best Customer Service</li>
</ul>
<ul class="abs checks" style="left:285px;top:1325px">
  <li><span class="tick"><svg width="8" height="8" viewBox="0 0 8 8"><polyline points="1,4 3.2,6 7,1.5" fill="none" stroke="#fff" stroke-width="1.5"/></svg></span>Mass emailing</li>
  <li><span class="tick"><svg width="8" height="8" viewBox="0 0 8 8"><polyline points="1,4 3.2,6 7,1.5" fill="none" stroke="#fff" stroke-width="1.5"/></svg></span>Fixed Fee Model</li>
  <li><span class="tick"><svg width="8" height="8" viewBox="0 0 8 8"><polyline points="1,4 3.2,6 7,1.5" fill="none" stroke="#fff" stroke-width="1.5"/></svg></span>Multiple Hire</li>
</ul>
<a class="abs read-more">Read More &gt;&gt;</a>

<h2 class="abs heading" style="left:562px;top:1185px">TESTIMONIALS</h2>
<div class="abs rule" style="left:562px;top:1226px;width:218px;height:1px"></div>
<div class="abs qmark" style="left:550px;top:1238px">&ldquo;</div>
<p class="abs quote">Lorem Ipsum is simply dummy text of the printing and typesetting industry. Lorem Ipsum has been the industry's standard dummy text ever since the 1500s, when an unknown printer took a galley of type and scrambled it to make a type specimen book...</p>
<div class="abs qmark" style="left:948px;top:1306px">&rdquo;</div>
<div class="abs avatar" role="img" aria-label="Portrait photo of the client giving the testimonial"></div>
<div class="abs person-name">ERIK LINDQVIST</div>
<div class="abs person-role">Business man</div>
<div class="abs dots"><span></span><span></span></div>

<!-- Customers -->
<h2 class="abs heading customer-title">OUR CUSTOMER</h2>
<div class="abs rule" style="left:479px;top:1604px;width:242px;height:1px"></div>
<svg class="abs" style="left:45px;top:1674px" width="12" height="26" viewBox="0 0 12 26"><polyline points="10,2 2,13 10,24" fill="none" stroke="#bbb" stroke-width="1.3"/></svg>
<svg class="abs" style="left:1140px;top:1674px" width="12" height="26" viewBox="0 0 12 26"><polyline points="2,2 10,13 2,24" fill="none" stroke="#bbb" stroke-width="1.3"/></svg>
<div class="abs client" style="left:100px">Quorlix</div>
<div class="abs client" style="left:305px">Vantrel</div>
<div class="abs client" style="left:511px">Brendaso</div>
<div class="abs client" style="left:717px">Miltova</div>
<div class="abs client" style="left:922px">Orsenik</div>

<!-- Contact band -->
<div class="abs contact-band"></div>
<div class="abs cb-item" style="left:85px;top:1804px">
  <span class="cb-icon"><svg width="14" height="18" viewBox="0 0 14 18"><path d="M7 1a6 6 0 0 1 6 6c0 4-6 10-6 10S1 11 1 7a6 6 0 0 1 6-6z" fill="none" stroke="#fff" stroke-width="1.6"/><circle cx="7" cy="7" r="2" fill="#fff"/></svg></span>
  <span style="font-size:12px;line-height:20px">Taku, 2200 Harbor Lane Suite 118<br>Northvale, VA 20100-4400</span>
</div>
<div class="abs cb-item" style="left:480px;top:1804px">
  <span class="cb-icon"><svg width="16" height="16" viewBox="0 0 16 16"><path d="M3 1l3 3-2 2c1 2 3 4 6 6l2-2 3 3-2 2C7 15 1 9 1 3z" fill="#fff"/></svg></span>
  <span>(555)-210-4800</span>
</div>
<div class="abs cb-item" style="left:732px;top:1804px">
  <span class="cb-icon"><svg width="16" height="16" viewBox="0 0 16 16" fill="none" stroke="#fff" stroke-width="1.4"><rect x="2" y="6" width="12" height="8" rx="1"/><rect x="5" y="2" width="6" height="4"/><line x1="5" y1="10" x2="11" y2="10"/></svg></span>
  <span>(555)-210-4800</span>
</div>
<div class="abs cb-item" style="left:984px;top:1804px">
  <span class="cb-icon"><svg width="16" height="12" viewBox="0 0 16 12" fill="none" stroke="#fff" stroke-width="1.4"><rect x="1" y="1" width="14" height="10" rx="1"/><polyline points="1,1 8,7 15,1"/></svg></span>
  <span style="font-size:12px">info@taku.com</span>
</div>

<!-- Footer -->
<div class="abs footer"></div>
<div class="abs brand footer-logo">Taku</div>
<p class="abs footer-text">Es simplemente el texto de relleno de las imprentas y archivos de texto. Lorem Ipsum ha sido el texto de relleno estándar de las industrias desde el año 1500</p>
<div class="abs divider" style="left:370px"></div>
<div class="abs divider" style="left:598px"></div>
<div class="abs divider" style="left:845px"></div>

<div class="abs" style="left:405px;top:1887px">
  <div class="col-title">QUICK LINKS</div><div class="col-rule"></div>
  <ul class="links"><li>Home</li><li>About us</li><li>Services</li><li>Solutions</li><li>Options</li></ul>
</div>
<div class="abs" style="left:630px;top:1887px">
  <div class="col-title">INFORMATION</div><div class="col-rule"></div>
  <ul class="links"><li>Hr and Strategy</li><li>IT Recruitment</li><li>Management Consulting</li><li>Privacy Policy</li><li>Terms &amp; Condition</li></ul>
</div>
<div class="abs" style="left:875px;top:1887px">
  <div class="col-title">CONTACT DETAILS</div><div class="col-rule" style="width:180px"></div>
</div>
<div class="abs map" role="img" aria-label="Street map showing the office location"></div>

<div class="abs bottom-bar"></div>
<div class="abs copyright">© Taku 2016. All right reserved</div>
<div class="abs social bottom-social"><span class="s1"></span><span class="s2"></span><span class="s3"></span></div>

</body>
</html>
```